Speisekarten-Design für Biergarten am Ufer des Bodensees
Super tolle Designerin. Vielen Dank Roswitha!
Zielgruppe
Wir sind ein direkt am Ufer des Bodensees liegender Biergarten, welcher seit über 30 Jahren besteht und deshalb fest in unserer Stadt verwurzelt ist. Zu unserer Zielgruppe gehören Touristen und Einheimische jeglicher Art - wir heißen einfach alle willkommen. Wir bieten unseren Gästen einfache Speisen und lokale Getränke. Uns ist wichtig, dass die Speise- & Getränkekarte das Gefühl von Heimat, Regionalität und Liebe zum Bodensee vermittelt. Wir bevorzugen ein modernes und klares Design, welches jedoch klassische Strukturen wie die eines typischen 60er-Jahre-Diners miteinbezieht.
Aufgabenstellung
Es wäre es toll, wenn diese Faltbar und kompakt (DIN-A4 evtl. etwas größer) ist. Die Textfelder sollten das komplette Speise- und Getränkeangebot darstellen (ca. 15 Gerichte, 6 Biersorten, 6 Softdrinks, 6 Heißgetränke). Wir bevorzugen warme Farbtöne. Es ist nicht notwendig Bilder in der Karte zu hinterlegen.

```html
<!DOCTYPE html>
<html lang="de">
<head>
<meta charset="utf-8">
<title>Gasthaus Uferlinde – Speisekarte</title>
<link href="https://fonts.googleapis.com/css2?family=Rye&family=Poppins:wght@200;300;400&family=Ubuntu:wght@700&display=swap" rel="stylesheet">
<style>
  :root {
    --backdrop: #4a5259;
    --wood-light: #a27b5c;
    --wood-mid: #8b6548;
    --wood-dark: #5e4230;
    --paper: #ffffff;
    --accent-red: #c8161d;
    --ink: #1e1e1e;
    --ink-soft: #444444;
    --on-wood: #ffffff;
  }
  * { box-sizing: border-box; margin: 0; padding: 0; }
  html, body { width: 1200px; height: 849px; overflow: hidden; }
  body { background: var(--backdrop); position: relative; font-family: "Poppins", sans-serif; }

  .wood {
    position: absolute;
    background:
      repeating-linear-gradient(180deg, transparent 0 118px, rgba(40,25,15,.55) 118px 121px, transparent 121px 130px),
      linear-gradient(180deg, var(--wood-light), var(--wood-mid) 55%, var(--wood-light) 100%);
    box-shadow: 0 6px 18px rgba(0,0,0,.35);
  }

  /* Inside spread */
  .spread { left: 40px; top: 162px; width: 740px; height: 524px; }
  .page {
    position: absolute; top: 45px; width: 332px; height: 335px;
    background: var(--paper); padding: 18px 20px;
    box-shadow: 0 3px 8px rgba(0,0,0,.25);
  }
  .page--food { left: 25px; }
  .page--drinks { left: 381px; }
  .page-title { font-family: "Rye", serif; color: var(--accent-red); font-size: 16px; font-weight: 400; margin-bottom: 14px; }
  .section-title { font-weight: 300; font-size: 10px; color: var(--ink-soft); margin-bottom: 10px; }
  .menu-list { list-style: none; width: 250px; margin-bottom: 18px; }
  .menu-item { display: flex; align-items: baseline; font-size: 9.6px; line-height: 12.7px; color: var(--ink); font-weight: 400; }
  .menu-item .num { font-weight: 300; color: var(--ink); }
  .leader { flex: 1; border-bottom: 1px dotted var(--ink-soft); margin: 0 1px 2px; }
  .leader--short { flex: 0 0 84px; }
  .menu-list--drinks { margin-bottom: 16px; }
  sup { font-size: 6px; }

  .claim {
    position: absolute; left: 22px; top: 400px;
    font-weight: 200; font-size: 58px; letter-spacing: -3px;
    color: var(--on-wood); white-space: nowrap; line-height: 1;
  }

  /* Cover */
  .cover { left: 810px; top: 162px; width: 350px; height: 524px; }
  .brand-name {
    position: absolute; left: 0; right: 0; top: 88px; text-align: center;
    color: var(--on-wood); font-size: 22px; font-weight: 300; letter-spacing: .5px;
  }
  .brand-line { position: absolute; left: 0; right: 0; top: 124px; text-align: center; color: var(--on-wood); font-weight: 300; font-size: 14px; }
  .cover-note {
    position: absolute; left: 0; right: 0; top: 222px; text-align: center;
    font-family: "Ubuntu", sans-serif; font-weight: 700; color: var(--on-wood);
    font-size: 14px; line-height: 1.3; text-shadow: 0 1px 3px rgba(0,0,0,.35);
  }
</style>
</head>
<body>

<section class="wood spread" role="img" aria-label="Innenseite der Karte auf Holzbrett-Hintergrund">
  <article class="page page--food">
    <h2 class="page-title">Speisen</h2>
    <h3 class="section-title">Für den großen Hunger</h3>
    <ul class="menu-list">
      <li class="menu-item"><span class="num">1.</span><span class="leader leader--short"></span><span>Name</span><span class="leader"></span><span>0,00 €</span></li>
      <li class="menu-item"><span class="num">2.</span><span class="leader leader--short"></span><span>Name</span><span class="leader"></span><span>0,00 €</span></li>
      <li class="menu-item"><span class="num">3.</span><span class="leader leader--short"></span><span>Name</span><span class="leader"></span><span>0,00 €</span></li>
      <li class="menu-item"><span class="num">4.</span><span class="leader leader--short"></span><span>Name</span><span class="leader"></span><span>0,00 €</span></li>
      <li class="menu-item"><span class="num">5.</span><span class="leader leader--short"></span><span>Name</span><span class="leader"></span><span>0,00 €</span></li>
      <li class="menu-item"><span class="num">6.</span><span class="leader leader--short"></span><span>Name</span><span class="leader"></span><span>0,00 €</span></li>
      <li class="menu-item"><span class="num">7.</span><span class="leader leader--short"></span><span>Name</span><span class="leader"></span><span>0,00 €</span></li>
    </ul>
    <h3 class="section-title">Für den kleinen Hunger</h3>
    <ul class="menu-list">
      <li class="menu-item"><span class="num">8.</span><span class="leader leader--short"></span><span>Name</span><span class="leader"></span><span>0,00 €</span></li>
      <li class="menu-item"><span class="num">9.</span><span class="leader leader--short"></span><span>Name</span><span class="leader"></span><span>0,00 €</span></li>
      <li class="menu-item"><span class="num">10.</span><span class="leader leader--short"></span><span>Name</span><span class="leader"></span><span>0,00 €</span></li>
      <li class="menu-item"><span class="num">11.</span><span class="leader leader--short"></span><span>Name</span><span class="leader"></span><span>0,00 €</span></li>
      <li class="menu-item"><span class="num">12.</span><span class="leader leader--short"></span><span>Name</span><span class="leader"></span><span>0,00 €</span></li>
      <li class="menu-item"><span class="num">13.</span><span class="leader leader--short"></span><span>Name</span><span class="leader"></span><span>0,00 €</span></li>
      <li class="menu-item"><span class="num">14.</span><span class="leader leader--short"></span><span>Name</span><span class="leader"></span><span>0,00 €</span></li>
      <li class="menu-item"><span class="num">15.</span><span class="leader leader--short"></span><span>Name</span><span class="leader"></span><span>0,00 €</span></li>
    </ul>
  </article>

  <article class="page page--drinks">
    <h2 class="page-title">Getränke</h2>
    <h3 class="section-title">Bier</h3>
    <ul class="menu-list menu-list--drinks">
      <li class="menu-item"><span>Name<sup>2,3</sup></span><span class="leader"></span><span>0,00 €</span></li>
      <li class="menu-item"><span>Name</span><span class="leader"></span><span>0,00 €</span></li>
      <li class="menu-item"><span>Name</span><span class="leader"></span><span>0,00 €</span></li>
    </ul>
    <h3 class="section-title">Softdrinks</h3>
    <ul class="menu-list menu-list--drinks">
      <li class="menu-item"><span>Name</span><span class="leader"></span><span>0,00 €</span></li>
      <li class="menu-item"><span>Name</span><span class="leader"></span><span>0,00 €</span></li>
      <li class="menu-item"><span>Name</span><span class="leader"></span><span>0,00 €</span></li>
    </ul>
    <h3 class="section-title">Heißgetränke</h3>
    <ul class="menu-list menu-list--drinks">
      <li class="menu-item"><span>Name</span><span class="leader"></span><span>0,00 €</span></li>
      <li class="menu-item"><span>Name</span><span class="leader"></span><span>0,00 €</span></li>
      <li class="menu-item"><span>Name</span><span class="leader"></span><span>0,00 €</span></li>
    </ul>
  </article>

  <p class="claim">EHRLICH. EINFACH. REGIONAL</p>
</section>

<section class="wood cover" role="img" aria-label="Titelseite der Karte auf Holzbrett-Hintergrund">
  <p class="brand-name">Gasthaus Uferlinde</p>
  <p class="brand-line">Ehrlich. Einfach. Regional</p>
  <p class="cover-note">Familienbetrieb direkt am Bodensee<br>seit über 30 Jahren</p>
</section>

</body>
</html>
```